RESTAURANT SIGN - copy the style provided !

A banner to put in front of an Italian Pizzeria.
See attached picture or link:
http://www.copperkestrelpress.com/wp-content/uploads/2013/12/VintaFlow.jpg

I want exactly the same colours, font, etc
The wording in the middle says 'PIZZERIA' and takes up a lot of the height.
- on the left in white with 2 dots either side: 'BY THE SLICE'(like 'HANDCRAFTED PIES'). On the other side 'AL TAGLIO'.
Canvas size 590cm long x 40cm High
(I will design the side of the canvas so can be left with background colour)

Industry/Entity Type

Restaurant

Font styles to use
Sans Serif

Colors
87cfc6
f37122
ffffff

Requirements
Must have
• Exactly as the given image. Simple!

```html
<!DOCTYPE html>
<html lang="it">
<head>
<meta charset="utf-8">
<title>Pizzeria Novella – Banner</title>
<link href="https://fonts.googleapis.com/css2?family=Oswald:wght@500;600&display=swap" rel="stylesheet">
<style>
  :root {
    --cream: #fdf8d8;
    --sign-red: #c8202e;
    --sign-shadow: #3a1012;
    --shopfront-dark: #3b3128;
    --shopfront-light: #8a7a62;
    --bakery-dark: #4a2f1c;
    --bakery-light: #c99a64;
    --crest-ring: #d6d6d6;
    --white: #ffffff;
  }
  html, body {
    margin: 0;
    padding: 0;
    width: 1200px;
    height: 82px;
    overflow: hidden;
    background: var(--white);
  }
  .banner {
    position: relative;
    width: 1200px;
    height: 82px;
    background: var(--cream);
    overflow: hidden;
  }
  .banner__art {
    position: absolute;
    inset: 0;
  }
  .banner__title {
    position: absolute;
    left: 300px;
    width: 600px;
    top: 0;
    height: 82px;
    margin: 0;
    display: flex;
    align-items: center;
    justify-content: center;
    font-family: "Oswald", "Arial Narrow", sans-serif;
    font-weight: 600;
    font-size: 62px;
    line-height: 1;
    letter-spacing: 4px;
    color: var(--sign-red);
    text-shadow: 2px 2px 0 var(--sign-shadow);
    white-space: nowrap;
  }
  .banner__tagline {
    position: absolute;
    top: 0;
    height: 82px;
    margin: 0;
    display: flex;
    align-items: center;
    justify-content: center;
    font-family: "Oswald", "Arial Narrow", sans-serif;
    font-weight: 500;
    font-size: 16px;
    letter-spacing: 2px;
    color: var(--white);
    white-space: nowrap;
  }
  .banner__tagline--left { left: 10px; width: 190px; }
  .banner__tagline--right { left: 1000px; width: 190px; }
</style>
</head>
<body>
  <div class="banner">
    <svg class="banner__art" width="1200" height="82" viewBox="0 0 1200 82">
      <defs>
        <linearGradient id="shopfront-tone" x1="0" y1="0" x2="1" y2="0">
          <stop offset="0" stop-color="#3b3128"/>
          <stop offset="0.5" stop-color="#8a7a62"/>
          <stop offset="1" stop-color="#3b3128"/>
        </linearGradient>
        <linearGradient id="bakery-tone" x1="0" y1="0" x2="0" y2="1">
          <stop offset="0" stop-color="#4a2f1c"/>
          <stop offset="0.6" stop-color="#c99a64"/>
          <stop offset="1" stop-color="#4a2f1c"/>
        </linearGradient>
        <radialGradient id="pizza-tone" cx="0.5" cy="0.5" r="0.5">
          <stop offset="0" stop-color="#e8c07a"/>
          <stop offset="0.6" stop-color="#c8402c"/>
          <stop offset="1" stop-color="#6b8a3a"/>
        </radialGradient>
      </defs>

      <path class="photo photo--shopfront" role="img" aria-label="Photo of the pizzeria shop front on a street"
            d="M0 0 H250 C285 0 300 30 300 41 C300 60 285 82 255 82 H0 Z"
            fill="url(#shopfront-tone)"/>

      <g class="crest" role="img" aria-label="City crest emblem">
        <circle cx="253" cy="41" r="39" fill="#ffffff" stroke="#d6d6d6" stroke-width="2"/>
        <circle cx="253" cy="41" r="28" fill="#7a8f6a"/>
      </g>

      <path class="photo photo--bakery" role="img" aria-label="Photo of a bakery counter with breads and pastries"
            d="M1200 0 H945 C915 0 900 25 900 41 C900 60 915 82 945 82 H1200 Z"
            fill="url(#bakery-tone)"/>

      <g class="pizza-medallion" role="img" aria-label="Round photo of pizza al taglio slices">
        <circle cx="956" cy="41" r="39" fill="#ffffff"/>
        <circle cx="956" cy="41" r="36" fill="url(#pizza-tone)"/>
      </g>
    </svg>

    <p class="banner__tagline banner__tagline--left">•• BY THE SLICE ••</p>
    <h1 class="banner__title">PIZZERIA NOVELLA</h1>
    <p class="banner__tagline banner__tagline--right">•• AL TAGLIO ••</p>
  </div>
</body>
</html>
```